Online Certificate in Research Methods needs a Digital Banner ad

We are launching an online graduate certificate in Quantitative and Qualitative Social Science Research Methods. We need a digital banner created so we can advertise on pagenook, seekora, and some other places.

The banner needs to use these color schemes and fonts: https://universityrelations.bmlu.edu/brand-guide/color

Would like the banner to say (either as three lines, or if not in three lines, have these sets of words at minimum on the same line):
Online Graduate Certificate in
Quantitative & Qualitative
Social Science Research Methods

We also want it to say Brennmoor Lake University and Next Start Date August 18, 2021. I’ve attached a picture of a version we tried to create but is hard to read.

We need a graphic that looks good in the following specs:
600px wide x 70px tall, high quality (at least 300 dpi) jpg or png

And
Pagenook recommendations:
Design Recommendations
• File Type: JPG or PNG
• Ratio: 1.91:1 to 1:1
• Resolution: At least 1080 x 1080 pixels
Text Recommendations
• Primary Text: 125 characters
• Headline: 40 characters
• Description: 30 characters
Technical Requirements
• Maximum File Size: 30MB
• Minimum Width: 600 pixels
• Minimum Height: 600 pixels
• Aspect Ratio Tolerance: 3%

```html
<!DOCTYPE html>
<html lang="en">
<head>
<meta charset="utf-8">
<title>Brennmoor Lake University – Research Methods Certificate Banners</title>
<link rel="stylesheet" href="https://fonts.googleapis.com/css2?family=Inter:wght@300;400;600;700&family=Archivo:wght@800&display=swap">
<style>
  :root {
    --stage: #808080;
    --navy: #060b36;
    --navy-deep: #040829;
    --navy-mid: #0f1a5c;
    --gold: #eaaa00;
    --white: #ffffff;
    --photo-warm: #8a5a4e;
    --photo-cool: #2f4c8f;
    --photo-light: #c9d4dc;
  }
  * { box-sizing: border-box; margin: 0; padding: 0; }
  html, body { width: 1200px; height: 1189px; overflow: hidden; }
  body {
    background: var(--stage);
    position: relative;
    font-family: "Inter", Arial, sans-serif;
    color: var(--white);
  }

  .ad { position: absolute; overflow: hidden; background: var(--navy); }
  .photo { position: absolute; }
  .wordmark { position: absolute; display: flex; align-items: flex-start; gap: 7px; }
  .wordmark-square { background: var(--gold); flex: none; }
  .wordmark-name { font-weight: 400; line-height: 1; white-space: nowrap; letter-spacing: -0.02em; }
  .wordmark-campus { display: block; font-weight: 400; letter-spacing: 0.01em; margin-top: 4px; }
  .headline { position: absolute; line-height: 1.2; white-space: nowrap; }
  .headline-intro { display: block; font-weight: 300; }
  .headline-program { display: block; font-family: "Archivo", "Arial Black", sans-serif; font-weight: 800; letter-spacing: 0.01em; }
  .start { position: absolute; display: flex; align-items: flex-end; }
  .start-label { display: block; color: var(--gold); font-weight: 400; }
  .start-date { display: block; font-weight: 700; line-height: 1.05; }
  .decor { position: absolute; inset: 0; }

  /* Leaderboard banner */
  .ad-leaderboard { left: 156px; top: 221px; width: 889px; height: 103px; }
  .ad-leaderboard .photo {
    left: 0; top: 0; width: 340px; height: 103px;
    background: linear-gradient(90deg, var(--photo-warm) 0%, #5a3a52 20%, var(--navy-mid) 60%, var(--navy) 100%);
  }
  .ad-leaderboard .wordmark { left: 72px; top: 35px; gap: 6px; }
  .ad-leaderboard .wordmark-square { width: 11px; height: 11px; margin-top: 2px; }
  .ad-leaderboard .wordmark-name { font-size: 14.5px; }
  .ad-leaderboard .wordmark-campus { font-size: 10.5px; margin-left: 36px; margin-top: 5px; }
  .ad-leaderboard .headline { left: 356px; top: 19px; font-size: 17px; }
  .ad-leaderboard .headline-program { font-size: 17.5px; }
  .ad-leaderboard .start { left: 703px; top: 36px; gap: 6px; }
  .ad-leaderboard .start-label { font-size: 10px; }
  .ad-leaderboard .start-date { font-size: 18px; }
  .ad-leaderboard .clock { width: 18px; height: 18px; margin-bottom: 1px; }

  /* Square social ad */
  .ad-square { left: 304px; top: 375px; width: 593px; height: 593px; }
  .ad-square .photo {
    left: 0; top: 0; width: 593px; height: 400px;
    background:
      linear-gradient(180deg, rgba(6,11,54,0) 62%, var(--navy) 100%),
      linear-gradient(100deg, var(--photo-light) 0%, var(--photo-warm) 25%, #6e3a44 42%, var(--photo-cool) 62%, #3c5aa0 80%, var(--photo-light) 100%);
  }
  .ad-square .wordmark { right: 20px; top: 20px; }
  .ad-square .wordmark-square { width: 15px; height: 15px; margin-top: 3px; }
  .ad-square .wordmark-name { font-size: 21px; }
  .ad-square .wordmark-campus { font-size: 14px; margin-left: 32px; margin-top: 9px; }
  .ad-square .headline { left: 76px; top: 382px; font-size: 26px; }
  .ad-square .headline-program { font-size: 27.5px; }
  .ad-square .start { left: 86px; top: 509px; gap: 8px; }
  .ad-square .start-label { font-size: 14px; }
  .ad-square .start-date { font-size: 24px; }
  .ad-square .clock { width: 24px; height: 24px; margin-bottom: 2px; }
</style>
</head>
<body>

<section class="ad ad-leaderboard" aria-label="Leaderboard banner">
  <div class="photo" role="img" aria-label="Photo of graduate students writing at desks in a classroom"></div>
  <svg class="decor" viewBox="0 0 889 103" aria-hidden="true">
    <polygon points="300,103 336,0 889,0 889,103" fill="#060b36"/>
    <polygon points="279,103 301,103 340,0 318,0" fill="#eaaa00"/>
    <polygon points="301,103 340,0 352,0 316,103" fill="#0f1a5c"/>
  </svg>
  <div class="wordmark">
    <span class="wordmark-square"></span>
    <span class="wordmark-name">Brennmoor Lake University<span class="wordmark-campus">HARLOW CAMPUS</span></span>
  </div>
  <h1 class="headline">
    <span class="headline-intro">Online Graduate Certificate in</span>
    <span class="headline-program">Quantitative &amp; Qualitative</span>
    <span class="headline-program">Social Science Research Methods</span>
  </h1>
  <div class="start">
    <svg class="clock" viewBox="0 0 20 20" aria-hidden="true">
      <circle cx="10" cy="10" r="10" fill="#eaaa00"/>
      <path d="M10 4.5V10.5L13.5 13" stroke="#060b36" stroke-width="2.2" fill="none" stroke-linecap="round"/>
    </svg>
    <p><span class="start-label">Next Start Date</span><span class="start-date">August 18, 2021</span></p>
  </div>
</section>

<section class="ad ad-square" aria-label="Square social ad">
  <div class="photo" role="img" aria-label="Photo of graduate students taking notes at desks in a classroom"></div>
  <svg class="decor" viewBox="0 0 593 593" aria-hidden="true">
    <polygon points="245,0 593,0 593,78 291,78" fill="#060b36"/>
    <polygon points="0,593 22,593 66,517 66,484" fill="#eaaa00"/>
    <polygon points="22,593 66,517 66,593" fill="#0f1a5c"/>
  </svg>
  <div class="wordmark">
    <span class="wordmark-square"></span>
    <span class="wordmark-name">Brennmoor Lake University<span class="wordmark-campus">HARLOW CAMPUS</span></span>
  </div>
  <h2 class="headline">
    <span class="headline-intro">Online Graduate Certificate in</span>
    <span class="headline-program">Quantitative &amp; Qualitative</span>
    <span class="headline-program">Social Science Research Methods</span>
  </h2>
  <div class="start">
    <svg class="clock" viewBox="0 0 20 20" aria-hidden="true">
      <circle cx="10" cy="10" r="10" fill="#eaaa00"/>
      <path d="M10 4.5V10.5L13.5 13" stroke="#060b36" stroke-width="2.2" fill="none" stroke-linecap="round"/>
    </svg>
    <p><span class="start-label">Next Start Date</span><span class="start-date">August 18, 2021</span></p>
  </div>
</section>

</body>
</html>
```